Road Construction Company needs business cards

We would like a new business card designed for our business.

We're a road construction company based in Qld, Australia.

Can the business card please have the following information on it.

Name: Brent Malvoy
Position: General Manager
Phone: 0471 592 304
Email: Brent.malvoy@quendix.com.au
Address: 87 Harrowgate Ave, Pindarra, QLD, 4000
Website: www.quendix.com.au

Visually we'd like the card to be professional and simple.

Attached is our logo.

Our website is www.quendix.com.au

Target Market(s)

Men aged 25-60

Contact Information for Business Card

As listed in project description

Font styles to use
Serif

Requirements
Must have
• Large logo on back of card

```html
<!DOCTYPE html>
<html lang="en">
<head>
<meta charset="utf-8">
<title>Quendix Business Card</title>
<link rel="stylesheet" href="https://fonts.googleapis.com/css2?family=Outfit:wght@400;500;700;800&display=swap">
<style>
  :root {
    --stage: #221f1f;
    --brand-blue: #0054a2;
    --ink-blue: #0a4f9e;
    --paper: #ffffff;
  }
  * { margin: 0; padding: 0; box-sizing: border-box; }
  html, body { width: 1200px; height: 1000px; overflow: hidden; }
  body {
    background: var(--stage);
    position: relative;
    font-family: "Outfit", sans-serif;
    color: var(--ink-blue);
  }
  .card {
    position: absolute;
    left: 211px;
    width: 734px;
    height: 419px;
  }
  .card-front { top: 78px; background: var(--brand-blue); }
  .card-back { top: 535px; background: var(--paper); }

  .front-panel {
    position: absolute;
    left: 99px; top: 151px;
    width: 543px; height: 144px;
    background: var(--paper);
    display: flex; align-items: center; justify-content: center;
  }
  .wordmark {
    font-weight: 800;
    color: var(--brand-blue);
    letter-spacing: 2px;
    line-height: 1;
  }
  .wordmark-large { font-size: 96px; }
  .wordmark-small {
    position: absolute;
    left: 49px; top: 185px;
    font-size: 44px;
  }

  .contact-name {
    position: absolute;
    left: 325px; top: 50px;
    font-size: 32px; font-weight: 700;
    letter-spacing: 1px;
    text-transform: uppercase;
  }
  .contact-role {
    position: absolute;
    left: 327px; top: 92px;
    font-size: 21px; font-weight: 400;
    letter-spacing: 1.2px;
    text-transform: uppercase;
  }
  .divider {
    position: absolute;
    left: 325px; top: 148px;
    width: 375px; height: 2px;
    background: var(--ink-blue);
  }
  .details { position: absolute; left: 323px; top: 188px; list-style: none; }
  .detail {
    display: flex; align-items: flex-start;
    font-size: 17.5px; font-weight: 500;
    letter-spacing: 1px; line-height: 22px;
    text-transform: uppercase;
    margin-bottom: 24px;
  }
  .detail-icon {
    width: 24px; height: 24px;
    margin-right: 16px;
    flex: none;
    fill: var(--ink-blue);
  }
</style>
</head>
<body>
  <section class="card card-front">
    <div class="front-panel">
      <span class="wordmark wordmark-large">QUENDIX</span>
    </div>
  </section>

  <section class="card card-back">
    <span class="wordmark wordmark-small">QUENDIX</span>

    <h1 class="contact-name">Brent Malvoy</h1>
    <p class="contact-role">General Manager</p>
    <div class="divider"></div>

    <ul class="details">
      <li class="detail">
        <svg class="detail-icon" viewBox="0 0 24 24"><path d="M12 1C7.6 1 4.5 4.3 4.5 8.5 4.5 14 12 23 12 23s7.5-9 7.5-14.5C19.5 4.3 16.4 1 12 1zm0 10.5a3 3 0 1 1 0-6 3 3 0 0 1 0 6z"/></svg>
        <span>87 Harrowgate Ave, Pindarra<br>QLD, 4000</span>
      </li>
      <li class="detail">
        <svg class="detail-icon" viewBox="0 0 24 24"><path d="M6.6 10.8a15.2 15.2 0 0 0 6.6 6.6l2.2-2.2c.3-.3.7-.4 1-.2 1.1.4 2.3.6 3.6.6.6 0 1 .4 1 1V20c0 .6-.4 1-1 1A17 17 0 0 1 3 4c0-.6.4-1 1-1h3.5c.6 0 1 .4 1 1 0 1.3.2 2.5.6 3.6.1.3 0 .7-.2 1z"/></svg>
        <span>0471 592 304</span>
      </li>
      <li class="detail">
        <svg class="detail-icon" viewBox="0 0 24 24"><path d="M2 5h20v14H2z M3.5 6.5 12 13l8.5-6.5" fill="none" stroke="#0a4f9e" stroke-width="2"/><path d="M2 5h20l-10 8z"/></svg>
        <span>Brent.malvoy@quendix.com.au</span>
      </li>
      <li class="detail">
        <svg class="detail-icon" viewBox="0 0 24 24" fill="none" stroke="#0a4f9e" stroke-width="2"><circle cx="12" cy="12" r="10"/><path d="M2 12h20M12 2c3 3 3 17 0 20M12 2c-3 3-3 17 0 20"/></svg>
        <span>www.quendix.com.au</span>
      </li>
    </ul>
  </section>
</body>
</html>
```